Packaging design - PROTEIN BALLS

PACKAGING
The packaging is a round carton roll, size: Ø73x180 mm, mockup sample enclosed, The label on the carton roll should have a size of 225x178 mm (width x height)

PRODUCT
Chrunchy, cheesy PROTEIN BALLS (100% pure cheese) with a huge amount of protein (65%), a lot of calcium and very low carbogydrates (3%). Diameter about 1.5 cm.

DESIGN
Since our customers are very sporty people, runner, bodybuilder, etc. The design must fit to this sporty customer segment.

FILES
We need the open data for InDesign with all fonts and pictures. If there are licenses tu buy, we will do it.

SUMMARY
1. SNACK
• Crunchy cheese balls with a diameter of about 1.5cm
• 3 different flavors: "Swiss Alpine Salt", "Provencale" and "Hot Chili"
• High in Protein (65%) and Calcium (2%)
• Low in carbohydrates (3%)

2. PACKAGING
• Carton roll, size: Ø73x180 mm
• Background can be every color, but we think a black one will be high premium.
• Maybe different sports are represented in the background, maybe also cheese
• Be creative
• Label applied, size: 225x178 mm

3. DESIGN
• Product name = (Cheese) PROTEIN BALLS
• 3 different colors for the 3 flavors "Swiss Alpine Salt", "Provencale" and "Hot Chili"
• HighProtein, High Calcium and LowCarb must be pointed out on the front
• Swissness: Swiss made must be pointed out
• fresh and young design, most customers are sporty people, pumper with a strong body awareness

TARGET CUSTOMER
Our main customers are extremely sporty people, who work very hard on their muscles and fitness, most of them are runners, cross fitnesser, bodybuilders, etc We will launch the product in fitness centers, in supplement shops and we are planning to make some stories with sporty influencer.

Serif
Sans Serif

• Cheese, naturalness, healthy, PROTEIN balls, muscles, Swissness must showed on the product.

```html
<!DOCTYPE html>
<html lang="en">
<head>
<meta charset="utf-8">
<title>Cheesy Protein Balls – Label</title>
<link rel="stylesheet" href="https://fonts.googleapis.com/css2?family=Exo+2:ital,wght@1,800;1,900&family=Saira+Semi+Condensed:wght@600;700&family=Source+Sans+3:wght@400&display=swap">
<style>
  :root {
    --backdrop: #3a3a3c;
    --label: #ffffff;
    --band: #545456;
    --ink: #4f4f51;
    --body-ink: #1e1e1e;
    --photo-light: #e2cf9c;
    --photo-mid: #d3bc85;
  }
  * { box-sizing: border-box; margin: 0; padding: 0; }
  html, body { width: 981px; height: 1200px; overflow: hidden; background: var(--backdrop); }
  .canvas { position: relative; width: 981px; height: 1200px; background: var(--backdrop); }

  .label { position: absolute; top: 110px; width: 360px; height: 979px; background: var(--label); overflow: hidden; }
  .label--front { left: 101px; }
  .label--back { left: 521px; }

  .product-photo {
    position: absolute;
    background: linear-gradient(90deg, var(--photo-mid), var(--photo-light) 50%, var(--photo-mid));
  }
  .product-photo--left { left: 7px; top: 11px; width: 88px; height: 690px; }
  .product-photo--right { left: 264px; top: 11px; width: 84px; height: 749px; }

  .name-band { position: absolute; left: 93px; top: 1px; width: 173px; height: 757px; }
  .name-band text { fill: #ffffff; font-family: "Exo 2", sans-serif; font-style: italic; }
  .name-band .band-title { font-size: 92px; font-weight: 900; }
  .name-band .band-sub { font-size: 31px; font-weight: 800; }

  .flavor { position: absolute; left: 0; width: 100%; top: 906px; text-align: center;
    font-family: "Saira Semi Condensed", sans-serif; font-weight: 700; font-size: 33px; color: var(--ink); line-height: 1; }
  .flavor { top: 796px; }
  .claims { position: absolute; left: 0; width: 100%; top: 851px; list-style: none; text-align: center;
    font-family: "Saira Semi Condensed", sans-serif; font-weight: 600; font-size: 18.5px; line-height: 21px; color: var(--ink); }
  .base-bar { position: absolute; left: 93px; top: 943px; width: 173px; height: 36px; background: var(--band); }

  .product-title { position: absolute; left: 0; width: 100%; top: 68px; text-align: center;
    font-family: "Exo 2", sans-serif; font-style: italic; font-weight: 900; color: var(--ink); line-height: 1; }
  .product-title span { display: block; }
  .product-title .t-cheesy { font-size: 66px; }
  .product-title .t-protein { font-size: 72px; margin-top: 2px; letter-spacing: 0; }
  .product-title .t-balls { font-size: 66px; margin-top: 2px; }

  .description { position: absolute; left: 0; right: 0; top: 342px; text-align: center; white-space: nowrap;
    font-family: "Source Sans 3", sans-serif; font-size: 17.5px; line-height: 23.6px; color: var(--body-ink); }
</style>
</head>
<body>
<main class="canvas">
  <section class="label label--front">
    <div class="product-photo product-photo--left" role="img" aria-label="Product photo: column of crunchy cheese protein balls"></div>
    <div class="product-photo product-photo--right" role="img" aria-label="Product photo: column of crunchy cheese protein balls"></div>
    <svg class="name-band" viewBox="0 0 173 757" width="173" height="757">
      <polygon points="0,0 173,0 173,757 0,724" fill="var(--band)"/>
      <text class="band-title" transform="translate(97,706) rotate(-90)" textLength="680" lengthAdjust="spacingAndGlyphs">Cheesy PROTEIN</text>
      <text class="band-sub" transform="translate(136,690) rotate(-90)" textLength="644" lengthAdjust="spacingAndGlyphs">Balls with a diameter of about 1.5cm</text>
    </svg>
    <h2 class="flavor">Swiss Alpine Salt</h2>
    <ul class="claims">
      <li>High in Protein (65%)</li>
      <li>Calcium (2%)</li>
      <li>Low in carbohydrates (3%)</li>
    </ul>
    <div class="base-bar"></div>
  </section>

  <section class="label label--back">
    <h1 class="product-title">
      <span class="t-cheesy">Cheesy</span>
      <span class="t-protein">PROTEIN</span>
      <span class="t-balls">balls</span>
    </h1>
    <p class="description">Lorem ipsum dolor sit amet,<br>consectetuer adipiscing elit, sed<br>diam nonummy nibh euismod<br>tincidunt ut laoreet dolore magna<br>aliquam erat volutpat. Ut wisi enim<br>ad minim veniam, quis nostrud<br>exerci tation ullamcorper suscipit<br>lobortis nisl ut aliquip ex ea<br>commodo consequat. Duis autem<br>vel eum iriure dolor in hendrerit in<br>vulputate velit esse molestie<br>consequat, vel illum dolore eu<br>feugiat nulla facilisis at vero eros et<br>accumsan et iusto odio dignissim<br>qui blandit praesent luptatum zzril<br>delenit augue duis dolore te<br>feugait nulla facilisi.<br>Lorem ipsum dolor sit amet, cons</p>
  </section>
</main>
</body>
</html>
```